Design a Website in Wordpress for an Australian Health Training Company in Health related courses

We require a WORDPRESS based Website (due to add on's we need to use for third party software) to replace our old site.
We offer national face to face delivery in medical reception, terminology and also administration.
The website will have around 6 pages and the ability to describe our main 6 courses (perhaps on the Courses page this may be tabs opening up to details for example?)
I have attached a previous sample of a Joomla site which was being developed (please do not feel you have to copy this - but I am just giving it as a sample - copying would be boring). But it gives an idea of look/feel and colours which may be suitable. Open to other ideas though.
I will provide some of the content, but would like the ability to finish the content myself.
Images and graphics are important. While a few medical photos re great - don't be tempted to us all pictures of doctors and nurses (although a couple would be good) - these are administrative courses so general corporate, eye catching visionary pictures of people in general are great. A medical type picture is also fine.
THE BOOKING system - will be via an ADD ON which will occur at the end of the project and is supplied by a third party software company (our student management system). This project will include up to 2 hours working with the Tech guys from the third party software to enable the ADD ON. If this ADD ON requires more time, we will pay hourly (although I do not expect it will).
Mostly a female market, many mature aged women target 25-45 yrs. Mixture of medical/health and corporate. Maybe a bit of mums returning to work and corporate inspiration.
It Company
Coded - Design and coding required
5+ page
Must have
- Wordpress
- Great graphics
- Interesting
- professional and clean
- Enquiry section (info Pak)
- Should have a University feel to it - Education
- Pages
- Home Page - About Us - Recruitment -Courses - Class Schedule - Traineeships Queensland Funding - Latest News Blog - Corporate Training- Contact us

```html
<!DOCTYPE html>
<html lang="en">
<head>
<meta charset="utf-8">
<title>Harwood Institute of Training</title>
<link href="https://fonts.googleapis.com/css2?family=Open+Sans:wght@400;600;700&family=Oswald:wght@500;600&family=Merriweather:wght@700;900&display=swap" rel="stylesheet">
<style>
:root{
  --navy:#34496e;
  --navy-dark:#2a3b5b;
  --navy-field:#4a5f85;
  --orange:#f5a142;
  --orange-dark:#e58f2b;
  --ink:#3c3c3c;
  --muted:#6b6b6b;
  --light:#f0f0f0;
  --white:#ffffff;
  --charcoal:#4a4a4a;
}
*{box-sizing:border-box;margin:0;padding:0}
html,body{width:1200px;height:2740px;overflow:hidden}
body{position:relative;font-family:"Open Sans",Arial,sans-serif;color:var(--ink);background:var(--white)}
.abs{position:absolute}

/* header */
.site-header{left:0;top:0;width:1200px;height:150px;border-top:5px solid var(--navy-dark);background:var(--white)}
.brand{left:128px;top:22px;width:150px;text-align:center;font-family:"Merriweather",Georgia,serif;font-weight:900;color:var(--navy);font-size:17px;line-height:21px;text-transform:uppercase}
.brand-mark{display:block;width:44px;height:44px;margin:8px auto 0;background:var(--navy)}
.search{left:621px;top:22px;width:155px;height:42px;border:1px solid #cfcfcf;display:flex;align-items:center;padding-left:14px;gap:10px;font-size:12px;color:#9a9a9a;letter-spacing:.5px}
.btn-info{left:789px;top:22px;width:135px;height:42px;background:var(--orange);color:var(--white)}
.btn-enrol{left:933px;top:22px;width:136px;height:42px;background:var(--navy);color:var(--white)}
.hbtn{display:flex;align-items:center;justify-content:center;gap:10px;font-weight:700;font-size:13px}
.main-nav{left:330px;top:88px;height:44px;display:flex;align-items:center;font-size:12px;line-height:15px;color:var(--navy)}
.main-nav a{display:flex;align-items:center;height:40px;padding:0 12px;border-left:1px solid #c9ced8;color:var(--navy);text-decoration:none}
.main-nav a:first-child{border-left:none}
.main-nav a.active{background:var(--navy);color:var(--white);padding:0 15px;font-weight:600}
.main-nav a.active + a{border-left:none}

/* hero */
.hero{left:0;top:150px;width:1200px;height:450px}
.hero-photo{position:absolute;inset:0;background:linear-gradient(100deg,#9fb4c9 0%,#d9e2ea 35%,#eef2f5 55%,#c9d6e2 80%,#8ca2bd 100%)}
.hero-title{left:0;top:446px;width:1200px;text-align:center;font-family:"Oswald",Arial,sans-serif;font-weight:600;font-size:36px;color:var(--white);letter-spacing:.5px;text-shadow:0 2px 4px rgba(0,0,0,.25)}
.hero-btn{left:522px;top:512px;width:150px;height:42px;background:var(--orange);color:var(--white);display:flex;align-items:center;justify-content:center;font-weight:700;font-size:15px;gap:6px}
.hero-arrow{top:349px;width:54px;height:54px;border-radius:50%;background:var(--navy-dark);display:flex;align-items:center;justify-content:center}

/* welcome */
.welcome{left:0;top:600px;width:1200px;height:378px;background:var(--white)}
.welcome-copy{left:132px;top:628px;width:553px}
.kicker{font-family:"Merriweather",Georgia,serif;font-weight:700;font-size:14px;color:var(--navy);letter-spacing:.5px}
.welcome-name{font-family:"Merriweather",Georgia,serif;font-weight:900;font-size:21px;line-height:25px;color:var(--navy);text-transform:uppercase;margin:6px 0 20px}
.welcome-copy p{font-size:11.5px;line-height:19px;color:var(--ink);margin-bottom:15px}
.btn-read{display:inline-flex;align-items:center;gap:6px;height:36px;padding:0 14px;background:var(--orange);color:var(--white);font-weight:700;font-size:13px;margin-top:6px}
.welcome-divider{left:734px;top:672px;width:1px;height:268px;background:#dcdcdc}
.welcome-brand{left:760px;top:730px;width:290px;text-align:center;font-family:"Merriweather",Georgia,serif;font-weight:900;color:var(--navy);font-size:22px;line-height:30px;text-transform:uppercase}
.welcome-brand .brand-mark{width:70px;height:70px;margin:0 auto 16px}

/* info band */
.band{left:0;top:978px;width:1200px;height:640px;background:linear-gradient(180deg,#3a4f74 0%,var(--navy) 50%,#31446a 100%)}
.section-title{font-family:"Merriweather",Georgia,serif;font-weight:700;font-size:17px;color:var(--orange);text-transform:uppercase;letter-spacing:.3px}
.courses{left:132px;top:1015px;width:530px}
.course-list{list-style:none;margin-top:24px}
.course-list li{display:flex;align-items:center;gap:16px;height:43px;color:var(--white);font-size:12.5px}
.dot-icon{width:28px;height:28px;border-radius:50%;background:var(--orange);display:flex;align-items:center;justify-content:center;flex:none}
.infopack{left:132px;top:1353px;width:530px}
.form-grid{display:grid;grid-template-columns:256px 256px;column-gap:15px;row-gap:16px;margin-top:26px}
.field{height:44px;background:var(--navy-field);color:#e3e8f0;font-size:12px;display:flex;align-items:center;gap:10px;padding:0 14px}
.field .chev{margin-left:auto}
.btn-send{height:44px;background:var(--orange);color:var(--white);font-weight:700;font-size:19px;display:flex;align-items:center;justify-content:center;letter-spacing:1px}
.why{left:736px;top:1015px;width:340px}
.why-item{position:absolute;left:0;width:340px;display:flex;gap:22px}
.why-icon{width:58px;height:58px;border-radius:50%;background:var(--orange);flex:none;display:flex;align-items:center;justify-content:center}
.why-item h3{font-size:12px;font-weight:700;color:var(--white);margin-bottom:6px;text-transform:uppercase}
.why-item p{font-size:10.5px;line-height:15px;color:#dfe4ec}

/* blog */
.blog{left:0;top:1618px;width:1200px;height:469px;background:var(--light)}
.blog-title{left:132px;top:1658px}
.blog-nav{left:1032px;top:1656px;display:flex;gap:14px}
.post{top:1732px;width:221px;height:311px;background:var(--white)}
.post-img{position:absolute;left:6px;top:0;width:209px;height:153px}
.post-date{position:absolute;left:88px;top:-31px;width:44px;height:44px;border-radius:50%;background:var(--white);text-align:center;font-family:"Oswald",Arial,sans-serif;color:var(--orange);font-size:17px;line-height:22px;padding-top:3px}
.post-date small{display:block;font-family:"Open Sans",Arial,sans-serif;font-size:8px;line-height:8px;color:var(--ink)}
.post-body{position:absolute;left:12px;top:166px;width:197px}
.post-body h4{font-size:11.5px;line-height:15px;font-weight:700;color:var(--navy);margin-bottom:8px}
.post-body p{font-size:10px;line-height:14px;color:var(--muted);text-align:justify}
.post-more{position:absolute;left:12px;top:278px;font-size:9px;font-weight:700;color:var(--orange)}

/* testimonials */
.testimonials{left:0;top:2087px;width:1200px;height:336px}
.testimonial-photo{position:absolute;inset:0;background:linear-gradient(90deg,#3f3f3f 0%,#575452 30%,#4c4a48 60%,#5d5955 85%,#3e3e3e 100%)}
.t-title{left:0;top:2126px;width:1200px;text-align:center;font-family:"Merriweather",Georgia,serif;font-weight:700;font-size:17px;color:var(--white)}
.t-rule{left:568px;top:2160px;width:64px;height:3px;background:var(--orange)}
.t-quote{left:154px;top:2172px;font-family:"Merriweather",Georgia,serif;font-size:70px;line-height:70px;color:#b5b5b5}
.t-text{left:230px;top:2182px;width:880px;text-align:center;font-size:11.5px;line-height:21px;color:#ececec}
.t-person{left:515px;top:2325px;display:flex;align-items:center;gap:18px;color:var(--white)}
.avatar{width:46px;height:46px;border-radius:50%;background:linear-gradient(160deg,#e9e4df,#c9bdb3);border:2px solid var(--white)}
.t-person b{display:block;font-size:12px;font-weight:700}
.t-person span{font-size:10px}
.t-arrow{top:2336px}

/* footer */
.site-footer{left:0;top:2423px;width:1200px;height:274px;background:var(--navy)}
.footer-brand{left:132px;top:2460px;width:190px;text-align:center;font-family:"Merriweather",Georgia,serif;font-weight:900;color:var(--white);font-size:16px;line-height:21px;text-transform:uppercase}
.footer-brand .brand-mark{background:var(--white);width:50px;height:50px;margin:12px auto 0}
.footer-divider{left:335px;top:2456px;width:1px;height:200px;background:#5c6f92}
.contact{left:362px;top:2462px;width:240px;color:var(--white)}
.footer-h{font-size:12px;font-weight:700;color:var(--white);text-transform:uppercase;margin-bottom:20px}
.contact h5{font-size:10.5px;font-weight:700;text-transform:uppercase;margin-bottom:3px}
.contact p{font-size:10.5px;margin-bottom:16px;color:#e3e8f0}
.enquiry{left:636px;top:2462px;width:434px}
.efield{position:absolute;height:35px;background:var(--navy-field);color:#e3e8f0;font-size:10.5px;padding:10px 12px}
.btn-submit{left:983px;top:2629px;width:86px;height:33px;background:var(--orange);color:var(--white);font-weight:700;font-size:12px;display:flex;align-items:center;justify-content:center}

/* bottom bar */
.bottom-bar{left:0;top:2697px;width:1200px;height:43px;background:var(--orange);display:flex;align-items:center;justify-content:space-between;padding:0 128px 0 137px;font-size:10px;color:var(--navy-dark)}
.social{display:flex;align-items:center;gap:8px}
.social i{display:block;width:20px;height:20px;border-radius:50%;background:var(--navy)}
.social span{margin-right:6px}
</style>
</head>
<body>

<header class="site-header abs">
  <div class="brand abs">Harwood Institute of Training<span class="brand-mark"></span></div>
  <div class="search abs">
    <svg width="12" height="12" viewBox="0 0 12 12"><circle cx="5" cy="5" r="3.8" fill="none" stroke="#9a9a9a" stroke-width="1.5"/><line x1="8" y1="8" x2="11.2" y2="11.2" stroke="#9a9a9a" stroke-width="1.5"/></svg>
    SEARCH
  </div>
  <div class="btn-info hbtn abs">
    <svg width="20" height="20" viewBox="0 0 20 20"><circle cx="10" cy="10" r="9" fill="#fff"/><rect x="9" y="8.5" width="2" height="6.5" fill="#f5a142"/><circle cx="10" cy="6" r="1.3" fill="#f5a142"/></svg>
    INFO PACK
  </div>
  <div class="btn-enrol hbtn abs">
    <svg width="14" height="20" viewBox="0 0 14 20"><rect x="1" y="1" width="12" height="18" rx="6" fill="none" stroke="#fff" stroke-width="1.6"/><line x1="7" y1="4" x2="7" y2="8" stroke="#fff" stroke-width="1.6"/></svg>
    ENROL NOW
  </div>
  <nav class="main-nav abs">
    <a class="active">Home</a>
    <a>About Us</a>
    <a>Recruitment</a>
    <a>Courses</a>
    <a>Class<br>Schedule</a>
    <a>Traineeships<br>Queensland Funding</a>
    <a>Latest<br>News Blog</a>
    <a>Corporate<br>Training</a>
    <a>Contact<br>us</a>
  </nav>
</header>

<section class="hero abs">
  <div class="hero-photo" role="img" aria-label="Bright training room photo: a presenter at a flip chart teaching a group of healthcare students"></div>
</section>
<div class="hero-arrow abs" style="left:35px">
  <svg width="14" height="14" viewBox="0 0 14 14"><polyline points="9,2 4,7 9,12" fill="none" stroke="#fff" stroke-width="2"/></svg>
</div>
<div class="hero-arrow abs" style="left:1098px">
  <svg width="14" height="14" viewBox="0 0 14 14"><polyline points="5,2 10,7 5,12" fill="none" stroke="#fff" stroke-width="2"/></svg>
</div>
<h1 class="hero-title abs">COURSES FOR BUSY PEOPLE</h1>
<div class="hero-btn abs">READ MORE
  <svg width="12" height="10" viewBox="0 0 12 10"><polyline points="1,1 5,5 1,9" fill="none" stroke="#fff" stroke-width="1.6"/><polyline points="6,1 10,5 6,9" fill="none" stroke="#fff" stroke-width="1.6"/></svg>
</div>

<section class="welcome abs"></section>
<div class="welcome-copy abs">
  <div class="kicker">WELCOME TO</div>
  <h2 class="welcome-name">Harwood Institute<br>of Training</h2>
  <p>Harwood is Australia's Leading Provider of Educational, Training and Support Services for the Medical and Dental industry - enabling students to be immediately skilled and 'Job Ready' for a career in Health.</p>
  <p>Harwood is a Registered Training Organisation offering specialised Medical Administration Training in over 15 locations Australia wide. Harwood have trained thousands of students the required knowledge and skills to become successful health care administrators.</p>
  <p>Our unique Short Medical Reception and Terminology Course and our Full Qualification is Nationally Accredited and the go-to recognised qualification in industry.</p>
  <div class="btn-read">READ MORE
    <svg width="12" height="10" viewBox="0 0 12 10"><polyline points="1,1 5,5 1,9" fill="none" stroke="#fff" stroke-width="1.6"/><polyline points="6,1 10,5 6,9" fill="none" stroke="#fff" stroke-width="1.6"/></svg>
  </div>
</div>
<div class="welcome-divider abs"></div>
<div class="welcome-brand abs"><span class="brand-mark"></span>Harwood Institute<br>of Training</div>

<section class="band abs"></section>
<div class="courses abs">
  <h2 class="section-title">List of Courses</h2>
  <ul class="course-list">
    <li><span class="dot-icon"><svg width="14" height="14" viewBox="0 0 14 14"><circle cx="7" cy="4.5" r="3" fill="#fff"/><path d="M1.5 13c0-3 2.5-5 5.5-5s5.5 2 5.5 5z" fill="#fff"/></svg></span>Medical Reception &amp; Terminology</li>
    <li><span class="dot-icon"><svg width="14" height="14" viewBox="0 0 14 14"><rect x="1" y="4" width="12" height="8" rx="1" fill="#fff"/><rect x="4.5" y="1.5" width="5" height="3" fill="none" stroke="#fff" stroke-width="1.3"/></svg></span>Cert III Business Administration (Medical)</li>
    <li><span class="dot-icon"><svg width="14" height="14" viewBox="0 0 14 14"><rect x="5" y="1" width="4" height="12" fill="#fff"/><rect x="1" y="5" width="12" height="4" fill="#fff"/></svg></span>Medical Terminology</li>
    <li><span class="dot-icon"><svg width="16" height="12" viewBox="0 0 16 12"><rect x="0.8" y="0.8" width="14.4" height="10.4" rx="1" fill="none" stroke="#fff" stroke-width="1.4"/><rect x="3" y="3" width="2" height="2" fill="#fff"/><rect x="7" y="3" width="2" height="2" fill="#fff"/><rect x="11" y="3" width="2" height="2" fill="#fff"/><rect x="4" y="7" width="8" height="2" fill="#fff"/></svg></span>Keyboard and Typing</li>
    <li><span class="dot-icon"><svg width="14" height="14" viewBox="0 0 14 14"><circle cx="7" cy="7" r="5.5" fill="none" stroke="#fff" stroke-width="1.4"/><path d="M1.5 7h11M7 1.5c-2.5 3-2.5 8 0 11M7 1.5c2.5 3 2.5 8 0 11" fill="none" stroke="#fff" stroke-width="1.1"/></svg></span>Harwood Online</li>
    <li><span class="dot-icon"><svg width="12" height="14" viewBox="0 0 12 14"><rect x="1" y="6" width="10" height="7" rx="1" fill="#fff"/><path d="M3 6V4a3 3 0 0 1 6 0v2" fill="none" stroke="#fff" stroke-width="1.5"/></svg></span>Confidentiality</li>
  </ul>
</div>

<div class="infopack abs">
  <h2 class="section-title">Email me an Info Pack</h2>
  <div class="form-grid">
    <div class="field"><svg width="11" height="11" viewBox="0 0 14 14"><circle cx="7" cy="4.5" r="3" fill="#e3e8f0"/><path d="M1.5 13c0-3 2.5-5 5.5-5s5.5 2 5.5 5z" fill="#e3e8f0"/></svg>Name</div>
    <div class="field"><svg width="12" height="9" viewBox="0 0 12 9"><rect x="0.6" y="0.6" width="10.8" height="7.8" fill="none" stroke="#e3e8f0" stroke-width="1.2"/><polyline points="0.6,0.6 6,5 11.4,0.6" fill="none" stroke="#e3e8f0" stroke-width="1.2"/></svg>E mail</div>
    <div class="field"><svg width="11" height="11" viewBox="0 0 11 11"><rect x="0.6" y="1.6" width="8.8" height="8.8" fill="none" stroke="#e3e8f0" stroke-width="1.2"/><line x1="4" y1="7" x2="10.4" y2="0.6" stroke="#e3e8f0" stroke-width="1.4"/></svg>Course<svg class="chev" width="14" height="9" viewBox="0 0 14 9"><polyline points="1,1 7,7 13,1" fill="none" stroke="#fff" stroke-width="1.8"/></svg></div>
    <div class="field"><svg width="11" height="11" viewBox="0 0 11 11"><circle cx="5.5" cy="5.5" r="5" fill="#e3e8f0"/></svg>State</div>
    <div class="field"><svg width="11" height="11" viewBox="0 0 12 12"><path d="M2 1l2.5 0 1 3-1.5 1c.8 1.6 1.8 2.6 3.4 3.4l1-1.5 3 1V11c-5 .3-9.7-4.4-9.4-10z" fill="#e3e8f0"/></svg>Mobile</div>
    <div class="btn-send">SEND</div>
  </div>
</div>

<div class="why abs">
  <h2 class="section-title">Why Harwood Institute ?</h2>
  <div class="why-item" style="top:50px">
    <span class="why-icon"><svg width="26" height="26" viewBox="0 0 26 26"><rect x="2" y="11" width="5" height="13" fill="#fff"/><path d="M9 12l5-9c2 0 3 1.5 2.5 3.5L15.5 10H23c1.5 0 2.3 1.4 1.8 2.6l-3.3 10c-.3.8-1 1.4-1.9 1.4H9z" fill="#fff"/></svg></span>
    <div><h3>Quality</h3><p>Harwood delivery quality, effective training facilitated by industry leaders. Just ask our students who rate us on average of 4.7 out of 5.</p></div>
  </div>
  <div class="why-item" style="top:147px">
    <span class="why-icon"><svg width="26" height="26" viewBox="0 0 26 26"><circle cx="13" cy="13" r="8" fill="none" stroke="#fff" stroke-width="4" stroke-dasharray="4 2.3"/><circle cx="13" cy="13" r="3.2" fill="#fff"/></svg></span>
    <div><h3>Experience</h3><p>Harwood is Australia's largest and leading providers of nationally recognised training in health administration – training from over 17 locations Australia wide.</p></div>
  </div>
  <div class="why-item" style="top:257px">
    <span class="why-icon"><svg width="26" height="26" viewBox="0 0 26 26"><polygon points="13,2 16.3,9.4 24.4,10.2 18.3,15.6 20,23.6 13,19.5 6,23.6 7.7,15.6 1.6,10.2 9.7,9.4" fill="#fff"/></svg></span>
    <div><h3>Value</h3><p>Our innovative teaching approach allows us to deliver exceptional training at affordable prices with no hidden extras.</p></div>
  </div>
  <div class="why-item" style="top:359px">
    <span class="why-icon"><svg width="26" height="26" viewBox="0 0 26 26"><rect x="3" y="12" width="20" height="11" fill="#fff"/><rect x="5" y="4" width="4" height="8" fill="#fff"/><rect x="11" y="7" width="4" height="5" fill="#fff"/></svg></span>
    <div><h3>Industry Recognised</h3><p>Harwood work hand in hand with industry to develop our core programme and consolidate the programme annually to keep the programme fresh and relevant.</p></div>
  </div>
  <div class="why-item" style="top:474px">
    <span class="why-icon"><svg width="26" height="26" viewBox="0 0 26 26"><rect x="3" y="5" width="4" height="3" fill="#fff"/><rect x="9" y="5" width="14" height="3" fill="#fff"/><rect x="3" y="11.5" width="4" height="3" fill="#fff"/><rect x="9" y="11.5" width="14" height="3" fill="#fff"/><rect x="3" y="18" width="4" height="3" fill="#fff"/><rect x="9" y="18" width="14" height="3" fill="#fff"/></svg></span>
    <div><h3>Great Job Results</h3><p>Harwood students get jobs! Our focus is to create job-ready students who are mentored to achieve their goals. Harwood also provide a recruitment service for industry and graduates.</p></div>
  </div>
</div>

<section class="blog abs"></section>
<h2 class="section-title blog-title abs">Latest Blog</h2>
<div class="blog-nav abs">
  <svg width="12" height="18" viewBox="0 0 12 18"><polyline points="10,2 3,9 10,16" fill="none" stroke="#2a3b5b" stroke-width="2.4"/></svg>
  <svg width="12" height="18" viewBox="0 0 12 18"><polyline points="2,2 9,9 2,16" fill="none" stroke="#2a3b5b" stroke-width="2.4"/></svg>
</div>

<article class="post abs" style="left:135px">
  <div class="post-img" role="img" aria-label="Photo of medical staff reviewing notes together" style="background:linear-gradient(135deg,#d9e6ef,#9cb9cf)"></div>
  <div class="post-date">25<small>JAN</small></div>
  <div class="post-body"><h4>Short Course Medical Reception Training,</h4><p>The Harwood Medical Receptionist Training program is geared towards gaining employment and as part...</p></div>
  <div class="post-more">READ MORE</div>
</article>
<article class="post abs" style="left:371px">
  <div class="post-img" role="img" aria-label="Photo of a scan image shown on a tablet" style="background:linear-gradient(135deg,#5e6670,#2c3136)"></div>
  <div class="post-date">14<small>JUNE</small></div>
  <div class="post-body"><h4>Contrary to popular belief, Lorem Ipsum is not.</h4><p>The Harwood Medical Receptionist Training program is geared towards gaining employment and as part...</p></div>
  <div class="post-more">READ MORE</div>
</article>
<article class="post abs" style="left:608px">
  <div class="post-img" role="img" aria-label="Photo of a patient monitor display" style="background:linear-gradient(135deg,#25406a,#0f1c33)"></div>
  <div class="post-date">13<small>FEB</small></div>
  <div class="post-body"><h4>The standard chunk of Lorem Ipsum used since.</h4><p>The Harwood Medical Receptionist Training program is geared towards gaining employment and as part...</p></div>
  <div class="post-more">READ MORE</div>
</article>
<article class="post abs" style="left:846px">
  <div class="post-img" role="img" aria-label="Photo of a medical form with a stethoscope" style="background:linear-gradient(135deg,#e6eef6,#7fa6cf)"></div>
  <div class="post-date">25<small>JAN</small></div>
  <div class="post-body"><h4>Lorem Ipsum is simply dummy text of the printinG.</h4><p>The Harwood Medical Receptionist Training program is geared towards gaining employment and as part...</p></div>
  <div class="post-more">READ MORE</div>
</article>

<section class="testimonials abs">
  <div class="testimonial-photo" role="img" aria-label="Dimmed photo of smiling graduates in a group"></div>
</section>
<h2 class="t-title abs">TESTIMONIALS</h2>
<div class="t-rule abs"></div>
<div class="t-quote abs">&ldquo;</div>
<p class="t-text abs">There are many variations of passages of Lorem Ipsum available, but the majority have suffered alteration in some form, by injected humour, or randomised words which don't look even slightly believable. If you are going to use a passage of Lorem Ipsum, you need to be sure there isn't anything embarrassing hidden in the middle of text. All the Lorem Ipsum generators on the Internet tend to repeat predefined chunks as necessary, making this the first true generator.</p>
<svg class="t-arrow abs" style="left:470px" width="14" height="24" viewBox="0 0 14 24"><polyline points="12,2 3,12 12,22" fill="none" stroke="#fff" stroke-width="2.6"/></svg>
<div class="t-person abs">
  <div class="avatar" role="img" aria-label="Portrait of the reviewer"></div>
  <div><b>DANIEL MARSH</b><span>Australia</span></div>
</div>
<svg class="t-arrow abs" style="left:720px" width="14" height="24" viewBox="0 0 14 24"><polyline points="2,2 11,12 2,22" fill="none" stroke="#fff" stroke-width="2.6"/></svg>

<footer class="site-footer abs"></footer>
<div class="footer-brand abs">Harwood Institute<br>of Training<span class="brand-mark"></span></div>
<div class="footer-divider abs"></div>
<div class="contact abs">
  <div class="footer-h">Contact Us</div>
  <h5>New South Wales, Victoria &amp; ACT</h5><p>1800 420 118</p>
  <h5>South Australia, Queensland, NT</h5><p>1800 420 276</p>
  <h5>Western Australia</h5><p>08 9312 4400</p>
</div>
<div class="enquiry abs"><div class="footer-h">Enquiry</div></div>
<div class="efield abs" style="left:638px;top:2488px;width:208px">Name</div>
<div class="efield abs" style="left:638px;top:2530px;width:208px">E mail</div>
<div class="efield abs" style="left:638px;top:2572px;width:208px">Phone</div>
<div class="efield abs" style="left:859px;top:2488px;width:210px;height:119px">Message</div>
<div class="btn-submit abs">SUBMIT</div>

<div class="bottom-bar abs">
  <div class="social"><span>Follow us on</span><i></i><i></i><i></i><i></i></div>
  <div>Copyrights @ 2016 All Rights Reserved</div>
</div>

</body>
</html>
```